Black card, Logo on front, in brushed silver, embossed or stamped
details centred on the back of the card written in Serif Old type face
Hotel
Amber Heron Hotel Motel (or smaller logo)
your hosts
Colin and Marisa Doyle
left bottom:
7 Harcourt Street
Brindlewood NSW 2799
right bottom:
P: 02 61739485
M: 0428 315 947
W: www.amberheronhotel.com.au
E: amberheronhotel@mailbox.example
facebook emblem: @AmberHeronHotel
instagram emblem: @amberheronhotel

```html
<!DOCTYPE html>
<html lang="en">
<head>
<meta charset="utf-8">
<title>Amber Heron Hotel – Business Card</title>
<link rel="stylesheet" href="https://fonts.googleapis.com/css2?family=Cinzel:wght@500&family=EB+Garamond:wght@400;600&display=swap">
<style>
  :root {
    --backdrop: #3a3a3a;
    --card: #050505;
    --silver: #b9b9b9;
    --silver-dim: #8d8d8d;
    --ink: #f2f2f2;
    --muted: #7b7b7b;
    --rule: #9a9a9a;
  }
  * { box-sizing: border-box; margin: 0; padding: 0; }
  html, body { width: 1200px; height: 900px; overflow: hidden; }
  body {
    background: var(--backdrop);
    position: relative;
    font-family: "EB Garamond", "Times New Roman", serif;
  }
  .card {
    position: absolute;
    width: 620px;
    height: 354px;
    background: var(--card);
    box-shadow: 0 18px 40px rgba(0,0,0,.55);
  }
  .card--front { left: 140px; top: 70px; }
  .card--back { left: 440px; top: 476px; }

  .brand__mark {
    width: 34px; height: 34px;
    border-radius: 50%;
    background: var(--silver-dim);
    flex: none;
  }
  .brand__name {
    font-family: "Cinzel", "Times New Roman", serif;
    font-weight: 500;
    color: var(--silver);
    letter-spacing: 1px;
    white-space: nowrap;
  }
  .brand__place {
    font-family: "Cinzel", "Times New Roman", serif;
    font-weight: 500;
    color: var(--silver-dim);
    white-space: nowrap;
  }

  /* Front: mark, name with place below, divider, HOTEL */
  .front-lockup {
    position: absolute; left: 0; right: 0; top: 140px;
    display: flex; align-items: center; justify-content: center; gap: 16px;
  }
  .front-lockup__text { display: flex; flex-direction: column; align-items: center; gap: 6px; }
  .front-lockup .brand__name { font-size: 28px; }
  .front-lockup .brand__place { font-size: 14px; letter-spacing: 6px; }
  .front-lockup__divider { width: 1px; height: 56px; background: var(--silver); }
  .front-lockup__word {
    font-family: "Cinzel", "Times New Roman", serif;
    font-weight: 500; color: var(--silver);
    font-size: 34px; letter-spacing: 1px;
  }

  /* Back */
  .back-lockup {
    position: absolute; left: 40px; top: 118px;
    width: 250px;
    display: flex; flex-direction: column; align-items: center; gap: 10px;
  }
  .back-lockup .brand__name { font-size: 28px; }
  .back-lockup .brand__place { font-size: 14px; letter-spacing: 6px; }

  .details {
    position: absolute; left: 318px; top: 40px;
    padding-left: 16px;
    border-left: 1px solid var(--rule);
    color: var(--ink);
    font-size: 14.5px;
    line-height: 1.32;
  }
  .details__hosts { font-weight: 600; font-size: 17px; }
  .details__role { color: var(--muted); margin-bottom: 2px; }
  .details__line { display: flex; align-items: center; gap: 8px; }
  .details__line svg { width: 11px; height: 11px; flex: none; }

  .rule-right {
    position: absolute; right: 0; top: 212px;
    width: 290px; height: 1px; background: var(--rule);
  }
  .social {
    position: absolute; left: 0; right: 0; bottom: 34px;
    display: flex; align-items: center; gap: 12px;
    color: var(--ink); font-size: 14.5px;
    padding-left: 70px;
  }
  .social__line { height: 1px; background: var(--rule); }
  .social__line--left { width: 110px; }
  .social__line--right { width: 70px; }
  .social__item { display: flex; align-items: center; gap: 6px; white-space: nowrap; }
  .social__badge { width: 11px; height: 11px; background: var(--silver-dim); }
</style>
</head>
<body>

<section class="card card--front" aria-label="Card front">
  <div class="front-lockup">
    <span class="brand__mark"></span>
    <div class="front-lockup__text">
      <span class="brand__name">Amber Heron</span>
      <span class="brand__place">BRINDLEWOOD</span>
    </div>
    <span class="front-lockup__divider"></span>
    <span class="front-lockup__word">HOTEL</span>
  </div>
</section>

<section class="card card--back" aria-label="Card back">
  <div class="back-lockup">
    <span class="brand__mark"></span>
    <span class="brand__name">Amber Heron</span>
    <span class="brand__place">BRINDLEWOOD</span>
  </div>

  <div class="details">
    <p class="details__hosts">Colin &amp; Marisa Doyle</p>
    <p class="details__role">Your Hosts</p>
    <p>7 Harcourt Street</p>
    <p>Brindlewood NSW 2799</p>
    <p class="details__line">
      <svg viewBox="0 0 12 12"><path d="M3 1l2 2.5-1.2 1.2a7 7 0 003.5 3.5L8.5 7 11 9l-1 2C5 11 1 7 1 2z" fill="#bbb"/></svg>
      02 61739485</p>
    <p class="details__line">
      <svg viewBox="0 0 12 12"><rect x="3" y="1" width="6" height="10" rx="1" fill="none" stroke="#bbb" stroke-width="1.2"/><circle cx="6" cy="9.2" r=".7" fill="#bbb"/></svg>
      0428 315 947</p>
    <p class="details__line">
      <svg viewBox="0 0 12 12"><circle cx="6" cy="6" r="2" fill="none" stroke="#bbb" stroke-width="1.2"/><path d="M8 4v3a1.5 1.5 0 003 0V6a5 5 0 10-2 4" fill="none" stroke="#bbb" stroke-width="1.2"/></svg>
      amberheronhotel@mailbox.example</p>
    <p class="details__line">
      <svg viewBox="0 0 12 12"><circle cx="6" cy="6" r="5" fill="none" stroke="#bbb" stroke-width="1.1"/><path d="M1 6h10M6 1c-2.5 3-2.5 7 0 10M6 1c2.5 3 2.5 7 0 10" fill="none" stroke="#bbb" stroke-width="1"/></svg>
      www.amberheronhotel.com.au</p>
  </div>

  <div class="rule-right"></div>

  <div class="social">
    <span class="social__line social__line--left"></span>
    <span class="social__item"><span class="social__badge"></span>@AmberHeronHotel</span>
    <span class="social__item"><span class="social__badge"></span>@amberheronhotel</span>
    <span class="social__line social__line--right"></span>
  </div>
</section>

</body>
</html>
```